Home Page for Quillmark

We need to design a new home page for Quillmark.com, a provider of B2B data for sales and marketing professionals.

The home page should follow the lead of our newly re-designed header and logo (still being tweaked) and use our new color scheme. Please refer to attached file. Please use this file as as the basis of the design for the rest or the home page. No part of the header or logo needs to be altered in this project.

All submissions should be clear, fresh, clean and simple in style. We like the look and feel of tallyvine.com, costharbor.com and pollwren.com. Please use them as references.

The main functions of the home page will be to tell the user about 1) the benefits and uses of Quillmark and 2) to get them to sign up.

Based upon the successful redesign of our homepage, we will also be redesigning our subscription page and our about us page in the coming weeks.

Target Market(s)

Sales and marketing professionals. Mostly 25 - 45 year old males.

Industry/Entity Type

Marketing

Requirements
Must have
• Items needed:

1A) There should be three main points highlighted 1) Fresh Data 2) Sales Intelligence 3) Increased Bottomline. There will be further text under these headers tbd. For style/feel reference the same device used by pollwren uses on its homepage.

1B) When you rollover these three items they should highlight and be clickable. The click will lead you to a header and paragraph about each that is further down the homepage (text tbd).

2) We also need a free trial and a sign up button. This button should move with you as you scroll up and down the homepage. Reference www.tallyvine.com.

3) We need a “Featured In” section. Also reference tallyvine.com. You can pull the content from quillmark.com’s current home page.

4) We also need a social media buttons section (chatterbox, peeper, orbitnet+ and workLoop)

```html
<!DOCTYPE html>
<html lang="en">
<head>
<meta charset="utf-8">
<title>Quillmark — Home</title>
<link rel="stylesheet" href="https://fonts.googleapis.com/css2?family=Arimo:wght@400;700&family=Open+Sans:wght@300&display=swap">
<style>
:root{
  --page:#f6f6f6;
  --ink:#1f2933;
  --muted:#8a8a8a;
  --orange:#ee6a12;
  --orange-light:#f7861f;
  --blue:#1aa7df;
  --blue-light:#3cc0ee;
  --nav:#cfe6f3;
  --bar:#2c2c2c;
  --card:#ffffff;
  --line:#e2e2e2;
  --veil:rgba(105,105,105,.55);
}
*{box-sizing:border-box;margin:0;padding:0}
html,body{width:1200px;height:963px;overflow:hidden}
body{position:relative;background:var(--page);font-family:"Arimo",Arial,sans-serif;color:var(--ink)}
.abs{position:absolute;white-space:nowrap}

/* header */
.header{left:0;top:0;width:1200px;height:85px;background:#fafafa}
.brand{left:252px;top:30px;display:flex;align-items:center;gap:10px;font-size:34px;font-weight:400;color:var(--blue)}
.brand-dot{width:26px;height:26px;border-radius:50%;background:var(--blue)}
.nav{left:0;top:85px;width:1200px;height:28px;background:var(--nav)}
.nav-tabs{left:255px;top:85px;display:flex;height:28px}
.nav-tabs span{padding:0 12px;line-height:28px;font-size:14px;font-weight:700;color:#fff;border-right:1px solid #e8f3f9}
.nav-tabs .active{background:#fff;color:#9aa;width:67px;text-align:center}
.search{left:716px;top:87px;width:254px;height:24px;border-radius:12px;background:#fff;font-size:11px;color:#aaa;padding:5px 12px}
.login{left:770px;top:0;width:196px;height:130px;background:#f7b58a;border-radius:0 0 6px 6px;padding:6px 16px}
.login p{font-size:11px;font-weight:700;color:#fff}
.login .field{height:24px;background:#fff;margin-top:13px;font-size:10px;color:#aaa;padding:6px 10px}

/* hero */
.hero{left:130px;top:145px;width:940px;height:323px;border-radius:4px;background:linear-gradient(110deg,#c9d5de 0%,#e9eef2 45%,#b9c6d1 100%)}
.hero-title{left:188px;top:230px;font-size:40px;font-weight:700;color:#fff;line-height:48px}
.hero-sub{left:188px;top:286px;font-family:"Open Sans",Arial,sans-serif;font-size:29px;font-weight:300;color:#fff;line-height:38px}
.hero-btn{left:182px;top:367px;width:153px;height:45px;border-radius:4px;background:var(--orange-light);color:#fff;font-size:18px;font-weight:700;text-align:center;line-height:45px}
.hero-arrow{top:269px;width:76px;height:76px;border-radius:50%;background:#fff;color:#bbb;font-size:26px;line-height:76px}
.features{top:483px;font-size:18px;font-weight:700;color:#555}
.feature-copy{font-size:13px;font-weight:400;color:#888;line-height:19px;width:260px;white-space:normal;margin-top:11px}
.feature-copy b{font-weight:700}
.veil{left:0;top:0;width:1200px;height:555px;background:var(--veil)}
.veil-label{left:0;top:503px;width:1200px;text-align:center;color:#fff;font-size:26px;font-weight:700}

/* sticky bar */
.sticky{left:120px;top:555px;width:960px;height:62px;background:var(--bar);border-radius:0 0 4px 4px}
.try-btn{left:137px;top:562px;width:154px;height:47px;border-radius:4px;background:linear-gradient(#f58220,#e3600c);color:#fff;font-size:18px;font-weight:700;text-align:center;line-height:47px}
.tour{left:303px;top:577px;font-size:16px;font-weight:700;color:#c9c9c9}
.signup{left:850px;top:555px;width:220px;height:35px;background:var(--orange);border-radius:0 0 4px 4px;color:#fff;font-size:12px;font-weight:700;display:flex;align-items:center;justify-content:center;gap:8px}
.signup-tab{left:937px;top:588px;width:47px;height:12px;background:var(--orange);border-radius:0 0 4px 4px}

/* cards */
.card{background:linear-gradient(#fff,#efefef);border:1px solid #e4e4e4;border-radius:4px;box-shadow:0 1px 3px rgba(0,0,0,.12)}
.quote-card{left:130px;top:636px;width:620px;height:81px}
.avatar{left:130px;top:624px;width:104px;height:104px;border-radius:50%;border:4px solid #fff;box-shadow:0 1px 4px rgba(0,0,0,.35);background:radial-gradient(circle at 50% 45%,#b9a391,#6b7a8c)}
.quote{left:230px;top:655px;width:440px;text-align:center;font-size:16px;font-weight:700}
.quote-by{left:230px;top:678px;width:440px;text-align:center;font-size:14px;color:var(--muted)}
.quote-by b{color:#555}
.blog-card{left:768px;top:636px;width:302px;height:81px;text-align:center}
.blog-card h3{margin-top:19px;font-size:16px;font-weight:700}
.blog-line{font-size:14px;color:var(--muted);margin-top:4px}
.blog-line b{color:#777}
.blog-line i{font-style:normal;color:var(--orange);font-weight:700;margin:0 10px}

.panel{top:743px;width:301px;height:146px;background:var(--card);border:1px solid #e6e6e6;border-radius:4px;overflow:hidden}
.panel h4{height:35px;background:linear-gradient(var(--blue-light),var(--blue));color:#fff;font-size:14px;font-weight:700;padding:9px 19px}
.panel ul{list-style:none;padding:13px 19px 0}
.panel li{font-size:14px;line-height:20px;color:var(--muted);white-space:nowrap}
.panel li em{font-style:normal;color:var(--orange);margin-right:8px;font-weight:700}
.alerts li{font-weight:700;color:#7a7a7a}
.news li b{color:#777}

/* footer */
.rule{left:130px;top:909px;width:939px;height:1px;background:var(--line)}
.copyright{left:130px;top:925px;width:299px;height:38px;background:#3a3a3a;border-radius:4px 4px 0 0;color:#ddd;font-size:13px;padding:10px 15px}
.copyright b{color:var(--blue-light);font-weight:700}
.footer-links{left:448px;top:933px;font-size:13px;color:var(--muted)}
.social{top:924px;height:24px;border-radius:3px}
.base{left:0;top:957px;width:1200px;height:6px;background:#333}
</style>
</head>
<body>
<header>
  <div class="abs header"></div>
  <div class="abs brand"><span class="brand-dot"></span>Quillmark</div>
  <div class="abs nav"></div>
  <nav class="abs nav-tabs"><span class="active">New</span><span>People</span><span>Companies</span><span>Downloads</span></nav>
  <div class="abs search">search</div>
  <div class="abs login">
    <p>Account Login &nbsp;|&nbsp; Free sign Up</p>
    <div class="field">username</div>
    <div class="field">password</div>
  </div>
</header>

<section>
  <div class="abs hero" role="img" aria-label="Photo of business people shaking hands across a desk"></div>
  <h1 class="abs hero-title">New Opportunities.</h1>
  <div class="abs hero-sub">Market Knowledge.</div>
  <div class="abs hero-btn">Try it free</div>
  <div class="abs hero-arrow" style="left:92px;text-align:right;padding-right:18px">&#10094;</div>
  <div class="abs hero-arrow" style="left:1032px;padding-left:16px">&#10095;</div>

  <div class="abs features" style="left:149px">Fresh Data<p class="feature-copy">Lorem ipsum dolor sit amet potent <b>adipiscing elit</b>. Nullam et tellus quam.</p></div>
  <div class="abs features" style="left:453px">Sales Intelligence<p class="feature-copy">Nullam dapibus tincidunt sed augue mollis orci et dui tempor.</p></div>
  <div class="abs features" style="left:772px">Increased Bottomline<p class="feature-copy">Nulla egestas, nisi et placerat imperdiet, tellus est <b>mattis</b> arcu, nec <b>ultricies</b> est.</p></div>

  <div class="abs veil"></div>
  <div class="abs veil-label">&lt;!-- SCROLLED AREA --!&gt;</div>
</section>

<div class="abs sticky"></div>
<div class="abs try-btn">Try it free</div>
<div class="abs tour">or Take the Tour</div>
<div class="abs signup-tab">
  <svg width="47" height="12" viewBox="0 0 47 12"><path d="M16 3 L23.5 7 L31 3" fill="none" stroke="#fff" stroke-width="2"/></svg>
</div>
<div class="abs signup">
  <svg width="14" height="14" viewBox="0 0 14 14"><circle cx="7" cy="4" r="3.5" fill="#fff"/><path d="M0 14 C0 8 14 8 14 14Z" fill="#fff"/></svg>
  Sing up / Login
</div>

<div class="abs card quote-card"></div>
<div class="abs avatar" role="img" aria-label="Portrait photo of the quoted sales executive"></div>
<div class="abs quote">"My sales have increased 25% due to your website."</div>
<div class="abs quote-by"><b>Daniel Mercer</b> Sales Executive Quillmark</div>

<div class="abs card blog-card">
  <h3>Blog:</h3>
  <p class="blog-line"><i>&#10094;</i><b>12/11:</b> Copyfield scores $2.5M<i>&#10095;</i></p>
</div>

<div class="abs panel alerts" style="left:130px">
  <h4>» TODAY'S ALERTS</h4>
  <ul>
    <li><em>+</em>Brightcast Gets $5M Funding</li>
    <li><em>+</em>Halvorn Optics Hires VP NA Sales</li>
    <li><em>+</em>Orbitlane Gets $20M Contract</li>
    <li><em>+</em>Announces Hiring Plan</li>
  </ul>
</div>
<div class="abs panel" style="left:449px">
  <h4>» EXECUTIVE LISTS</h4>
  <ul>
    <li><em>✔</em>Emails included</li>
    <li><em>✔</em>Top US Company Executives</li>
    <li><em>✔</em>See our Delivery Guarantee</li>
    <li><em>✔</em>CEO, CFO, COO, VP, etc</li>
  </ul>
</div>
<div class="abs panel news" style="left:768px">
  <h4>» NEWS/AWARDS</h4>
  <ul>
    <li><em style="margin-right:3px">&gt;</em><b>11/27: 2012</b> Technology 200!</li>
    <li><em style="margin-right:3px">&gt;</em><b>07/17: 2012</b> Colorado Awardees</li>
    <li><em style="margin-right:3px">&gt;</em><b>07/03: 2012</b> Pennsylvania Awardees</li>
    <li><em style="margin-right:3px">&gt;</em><b>06/19: 2012</b> Midwest Awardees</li>
  </ul>
</div>

<footer>
  <div class="abs rule"></div>
  <div class="abs copyright">© Copyright 2013 <b>Quillmark</b>. Rights Reserved.</div>
  <div class="abs footer-links">People | Companies | SiteMap</div>
  <div class="abs social" style="left:941px;width:24px;background:#3b5a99" aria-label="chatterbox"></div>
  <div class="abs social" style="left:973px;width:24px;background:#2fa8dc" aria-label="peeper"></div>
  <div class="abs social" style="left:1004px;width:36px;background:#d9483b" aria-label="orbitnet+"></div>
  <div class="abs social" style="left:1046px;width:24px;background:#1f7bb6" aria-label="workLoop"></div>
  <div class="abs base"></div>
</footer>
</body>
</html>
```